Webdesign für Sportbegeisterte Firma
Zielgruppe
Wir sind eine Sportbegeisterte Firma und suchen ein hochwertiges responsives Design. Unsere Zielgruppe sind alle sportbegeisterte von jung bis alt.
Aufgabenstellung
Ich arbeite derzeit mit dem Design Quellwerk PLUS in Wordpress und würde mich freuen, wenn daran alles angepasst wird.

```html
<!DOCTYPE html>
<html lang="de">
<head>
<meta charset="utf-8">
<title>Lindner Sportwetten</title>
<link rel="stylesheet" href="https://fonts.googleapis.com/css2?family=Roboto:wght@400;500&family=Lato:wght@400;700&family=Roboto+Condensed:wght@400;700&display=swap">
<style>
:root{
  --green:#a4bf47;
  --yellow:#e2c341;
  --blue:#5ab8e8;
  --dark:#222;
  --text:#555;
  --muted:#777;
  --card-grey:#d6d6d6;
  --footer-grey:#f2f2f2;
}
*{margin:0;padding:0;box-sizing:border-box}
html,body{width:1200px;height:2758px;overflow:hidden}
body{position:relative;background:#fff;font-family:Lato,sans-serif;color:var(--text)}
.abs{position:absolute}
.center{text-align:center}

/* hero */
.hero{left:0;top:0;width:1200px;height:632px;background:radial-gradient(ellipse at 82% 35%,#a8371c 0%,#5a1c10 28%,transparent 55%),linear-gradient(160deg,#16171c 0%,#1c1c22 45%,#2a1d16 70%,#3a2418 100%)}
.hero-band{left:0;top:632px;width:1200px;height:6px;background:var(--green)}
.brand{font-family:Lato,sans-serif;font-weight:700;font-size:30px;color:var(--green);letter-spacing:.5px}
.nav a{position:absolute;top:36px;font-family:'Roboto Condensed',sans-serif;font-size:15px;color:#fff;text-decoration:none;line-height:18px}
.nav .active{left:778px;top:32px;width:64px;height:27px;border-radius:14px;background:var(--yellow);text-align:center;line-height:27px}
.hero h1{left:68px;top:200px;font-family:Roboto,sans-serif;font-weight:400;color:#fff;line-height:1}
.hero h1 .small{display:block;font-size:30px}
.hero h1 .big{display:block;font-size:46px;font-weight:500;margin-top:9px}
.hero-text{left:68px;top:290px;width:730px;font-family:Roboto,sans-serif;font-size:12.5px;line-height:17px;color:#fff}
.btn-yellow{left:68px;top:381px;width:161px;height:32px;border-radius:16px;background:var(--yellow);color:#fff;font-size:12px;text-align:center;line-height:32px}
.dot{top:537px;width:9px;height:9px;border-radius:50%;background:#fff}
.dot.ring{background:transparent;border:1.5px solid #fff}

/* feature cards */
.feature{top:731px;width:244px;height:225px;background:#fff;box-shadow:0 10px 28px rgba(0,0,0,.09)}
.feature .art{position:absolute;left:62px;top:18px;width:120px;height:86px;border-radius:43px;background:linear-gradient(135deg,#eef0f6,#d9dcec)}
.feature h3{position:absolute;top:121px;width:100%;text-align:center;font-size:11.5px;font-weight:700;color:#333;letter-spacing:.4px}
.feature p{position:absolute;top:145px;left:30px;width:184px;text-align:center;font-size:9.5px;line-height:15px;color:#555}

/* section headings */
.sec-title{width:1200px;left:0;text-align:center;font-family:Roboto,sans-serif;color:#333;font-size:21px;font-weight:400}
.sec-sub{width:1200px;left:0;text-align:center;font-size:9.5px;line-height:15px;color:#666}

/* team */
.member{top:1142px;width:206px;height:349px;background:var(--card-grey)}
.member.featured{background:var(--green);box-shadow:0 6px 18px rgba(0,0,0,.18);border:2px solid #fff}
.member .photo{position:absolute;left:17px;top:24px;width:171px;height:171px;border-radius:50%;border:3px solid #fff;background:linear-gradient(160deg,#c9b4a2,#7d6252)}
.member .name{position:absolute;top:229px;width:100%;text-align:center;font-family:'Roboto Condensed',sans-serif;font-weight:700;font-size:14px;color:var(--green)}
.member.featured .name,.member.featured .job,.member.featured .bio{color:#fff}
.member .job{position:absolute;top:250px;width:100%;text-align:center;font-size:9px;font-style:italic;font-weight:700;color:#666}
.member .bio{position:absolute;top:270px;left:15px;width:176px;text-align:center;font-size:9.5px;line-height:15px;color:#777}
.member .social{position:absolute;top:316px;left:0;width:100%;display:flex;justify-content:center;gap:18px}
.member .social span{width:7px;height:7px;border-radius:50%;background:#444}
.member.featured .social span{background:#fff}

/* testimonials */
.avatar{border-radius:50%;background:linear-gradient(160deg,#d7c9bd,#6f6259)}
.client-name{left:0;width:1200px;top:1781px;text-align:center;font-family:Roboto,sans-serif;font-weight:500;font-size:15px;letter-spacing:1.5px;color:#222}
.quote{left:490px;width:220px;top:1810px;text-align:center;font-size:9.5px;line-height:15px;color:#222}
.stars{left:563px;top:1868px;width:80px;display:flex;justify-content:space-between}

/* satisfaction */
.gauge-label{width:146px;text-align:center}
.gauge-num{font-family:Lato,sans-serif;font-size:34px;line-height:1}
.gauge-num small{font-size:11px}
.gauge-cap{font-size:8px;margin-top:6px}

/* footer */
.footer{left:0;top:2304px;width:600px;height:402px;background:var(--footer-grey)}
.map{left:600px;top:2304px;width:600px;height:402px;background:linear-gradient(135deg,#dcdcdc,#ededed 45%,#d2d2d2)}
.f-head{left:68px;top:2423px;font-size:11.5px;font-weight:700;color:#222;letter-spacing:.3px}
.f-addr{left:68px;top:2448px;font-size:9px;line-height:13.5px;color:#333}
.f-addr b{font-weight:700}
.f-contact{left:286px;font-size:8.5px;color:#333}
.f-contact b{font-weight:700;margin-right:6px}
.field{background:#fff;border:1px solid #e4e4e4;font-size:8px;color:#999;padding:6px 11px}
.btn-send{left:68px;top:2652px;width:89px;height:27px;border-radius:14px;background:var(--green);color:#fff;font-size:12px;font-weight:700;letter-spacing:2px;text-align:center;line-height:27px}
.bottom-bar{left:0;top:2706px;width:1200px;height:52px;background:var(--green)}
.copy{left:68px;top:2724px;font-family:Roboto,sans-serif;font-size:9.5px;color:#fff}
.bottom-nav{right:68px;top:2724px;font-size:8.5px;font-weight:700;color:#fff;letter-spacing:.4px}
.bottom-nav span{margin:0 10px}
</style>
</head>
<body>

<header>
  <div class="abs hero" role="img" aria-label="Nachtaufnahme einer Autobahn mit Lichtspuren vor einem rot beleuchteten Stadion"></div>
  <div class="abs hero-band"></div>
  <div class="abs brand" style="left:68px;top:28px">Lindner Sportwetten</div>
  <nav class="nav">
    <a class="active">START</a>
    <a style="left:867px">WETTTIPPS</a>
    <a style="left:974px">ÜBER UNS</a>
    <a style="left:1073px">STATISTIK</a>
  </nav>
  <div class="hero">
    <h1 class="abs"><span class="small">WILLKOMMEN BEI</span><span class="big">LINDNER SPORTWETTEN</span></h1>
    <p class="abs hero-text">Sportwetten-Tipps bequem online bei einem Buchmacher Ihrer Wahl abgeben. Egal ob Fußball, Eishcokey, oder Dart. Wir bieten Ihnen ein umfangreiches Angebot in fast allen Sportgategorien. Es sind keine besonderen Kenntnisse notwendig. Die Arbeit der Prognosen-Berechnung übernehmen wir für Sie. Ich bieten Ihnen zusätzlich unterschiedliche Mitgliedschaften mit unterschiedlichen Laufzeiten an. Jetzt einfach Mitgleid werden und von meinen Tipps profitieren. Viel Spaß beim Wetten!</p>
    <div class="abs btn-yellow">Zu den Mitgliedscahften</div>
    <span class="abs dot ring" style="left:578px"></span>
    <span class="abs dot" style="left:596px"></span>
    <span class="abs dot" style="left:614px"></span>
  </div>
</header>

<section class="features">
  <div class="abs feature" style="left:181px">
    <div class="art" role="img" aria-label="Illustration einer Person mit Münzen und Globen"></div>
    <h3>MONEYMANAGEMENT</h3>
    <p>Lorem ipsum dolor sit amet, consectetur adipiscing elit, sed do eiusmod tempor incididunt ut magna aliqua.</p>
  </div>
  <div class="abs feature" style="left:479px">
    <div class="art" role="img" aria-label="Illustration einer Supportmitarbeiterin am Laptop"></div>
    <h3>SUPPORT</h3>
    <p>Lorem ipsum dolor sit amet, consectetur adipiscing elit, sed do eiusmod tempor incididunt ut magna aliqua.</p>
  </div>
  <div class="abs feature" style="left:774px">
    <div class="art" role="img" aria-label="Illustration eines Balkendiagramms mit Person"></div>
    <h3>STATISTIK</h3>
    <p>Lorem ipsum dolor sit amet, consectetur adipiscing elit, sed do eiusmod tempor incididunt ut magna aliqua.</p>
  </div>
</section>

<section class="team">
  <h2 class="abs sec-title" style="top:1046px">Unser Team</h2>
  <p class="abs sec-sub" style="top:1076px">Hier könnt ihr euch selbst ein Bild von unserem Team machen. Wir arbeiten jeden Tag sehr hart,<br>damit ihr es so einfach wie möglich habt und versuchen uns immer weiter zu verbessern.</p>

  <div class="abs member" style="left:162px">
    <div class="photo" role="img" aria-label="Porträtfoto Teammitglied"></div>
    <div class="name">TEAM MEMBER NAME</div><div class="job">Team Member Job</div>
    <p class="bio">Mauris eleifend massa quis lacus ultricies auctor vel eget ligula. Integer.</p>
    <div class="social"><span></span><span></span><span></span><span></span></div>
  </div>
  <div class="abs member" style="left:381px">
    <div class="photo" role="img" aria-label="Porträtfoto Teammitglied"></div>
    <div class="name">TEAM MEMBER NAME</div><div class="job">Team Member Job</div>
    <p class="bio">Mauris eleifend massa quis lacus ultricies auctor vel eget ligula. Integer.</p>
    <div class="social"><span></span><span></span><span></span><span></span></div>
  </div>
  <div class="abs member featured" style="left:600px">
    <div class="photo" style="left:15px;top:22px" role="img" aria-label="Porträtfoto Teammitglied"></div>
    <div class="name" style="top:227px">TEAM MEMBER NAME</div><div class="job" style="top:248px">Team Member Job</div>
    <p class="bio" style="left:13px;top:268px">Mauris eleifend massa quis lacus ultricies auctor vel eget ligula. Integer.</p>
    <div class="social" style="top:314px"><span></span><span></span><span></span><span></span></div>
  </div>
  <div class="abs member" style="left:819px">
    <div class="photo" role="img" aria-label="Porträtfoto Teammitglied"></div>
    <div class="name">TEAM MEMBER NAME</div><div class="job">Team Member Job</div>
    <p class="bio">Mauris eleifend massa quis lacus ultricies auctor vel eget ligula. Integer.</p>
    <div class="social"><span></span><span></span><span></span><span></span></div>
  </div>
</section>

<section class="reviews">
  <h2 class="abs sec-title" style="top:1553px">KUNDENBEWERTUNGEN</h2>
  <p class="abs sec-sub" style="top:1588px">Ihr könnt euch auf uns verlassen<br>das sagen unsere Kunden:</p>
  <svg class="abs" style="left:278px;top:1709px" width="16" height="22" viewBox="0 0 16 22"><path d="M12 2 L4 11 L12 20" fill="none" stroke="var(--yellow)" stroke-width="4"/></svg>
  <svg class="abs" style="left:906px;top:1709px" width="16" height="22" viewBox="0 0 16 22"><path d="M4 2 L12 11 L4 20" fill="none" stroke="var(--yellow)" stroke-width="4"/></svg>
  <div class="abs avatar" style="left:424px;top:1694px;width:59px;height:59px" role="img" aria-label="Kundenfoto"></div>
  <div class="abs avatar" style="left:559px;top:1681px;width:84px;height:84px" role="img" aria-label="Kundenfoto"></div>
  <div class="abs avatar" style="left:716px;top:1694px;width:59px;height:59px" role="img" aria-label="Kundenfoto"></div>
  <div class="abs client-name">Jonas K.</div>
  <p class="abs quote">Bin schon seit 5 jahren dabei, die beste Seite wenn es um Sportwetten-Tipps geht. Bis heute vermutlich ein Geheimtipp.</p>
  <div class="abs stars">
    <svg width="11" height="11" viewBox="0 0 10 10"><path d="M5 0l1.2 3.6H10L7 5.8l1.1 3.7L5 7.3 1.9 9.5 3 5.8 0 3.6h3.8z" fill="var(--green)"/></svg>
    <svg width="11" height="11" viewBox="0 0 10 10"><path d="M5 0l1.2 3.6H10L7 5.8l1.1 3.7L5 7.3 1.9 9.5 3 5.8 0 3.6h3.8z" fill="var(--green)"/></svg>
    <svg width="11" height="11" viewBox="0 0 10 10"><path d="M5 0l1.2 3.6H10L7 5.8l1.1 3.7L5 7.3 1.9 9.5 3 5.8 0 3.6h3.8z" fill="var(--green)"/></svg>
    <svg width="11" height="11" viewBox="0 0 10 10"><path d="M5 0l1.2 3.6H10L7 5.8l1.1 3.7L5 7.3 1.9 9.5 3 5.8 0 3.6h3.8z" fill="var(--green)"/></svg>
    <svg width="11" height="11" viewBox="0 0 10 10"><path d="M5 0l1.2 3.6H10L7 5.8l1.1 3.7L5 7.3 1.9 9.5 3 5.8 0 3.6h3.8z" fill="var(--green)"/></svg>
  </div>
</section>

<section class="satisfaction">
  <h2 class="abs sec-title" style="top:1953px">KUNDENZUFRIEDENHEIT</h2>
  <p class="abs sec-sub" style="top:1988px">Sed ut perspiciatis unde omnis iste natus error sit voluptatem<br>accusantium doloremque laudantium.</p>
  <svg class="abs" style="left:0;top:2048px" width="1200" height="160">
    <g fill="none" stroke-width="3">
      <circle cx="409" cy="80" r="72" stroke="#eee"/>
      <circle cx="409" cy="80" r="72" stroke="var(--yellow)" stroke-dasharray="226 453" transform="rotate(90 409 80)"/>
      <circle cx="603" cy="80" r="72" stroke="#eee"/>
      <circle cx="603" cy="80" r="72" stroke="var(--green)" stroke-dasharray="339 453" transform="rotate(-40 603 80)"/>
      <circle cx="790" cy="80" r="72" stroke="var(--blue)" stroke-dasharray="440 453" transform="rotate(-80 790 80)"/>
    </g>
  </svg>
  <div class="abs gauge-label" style="left:336px;top:2100px;color:var(--yellow)"><div class="gauge-num">50<small>%</small></div><div class="gauge-cap">Mit positiver Bewertung</div></div>
  <div class="abs gauge-label" style="left:530px;top:2100px;color:var(--green)"><div class="gauge-num">75<small>%</small></div><div class="gauge-cap">Zufriedene Kunden</div></div>
  <div class="abs gauge-label" style="left:717px;top:2100px;color:var(--blue)"><div class="gauge-num">99<small>%</small></div><div class="gauge-cap">erneuern Ihre Mitgliedschaft</div></div>
</section>

<footer>
  <div class="abs footer"></div>
  <div class="abs map" role="img" aria-label="Stadtplan mit Standortmarkierung"></div>
  <div class="abs brand" style="left:68px;top:2355px">Lindner Sportwetten</div>
  <div class="abs f-head">KONTAKT INFORMATIONEN</div>
  <p class="abs f-addr"><b>Talweg 12</b><br>Talweg 12, 97300 Musterbach,<br>Germany</p>
  <p class="abs f-contact" style="top:2447px"><b>E-mail</b>info@lindner-sportwetten.example</p>
  <p class="abs f-contact" style="top:2467px"><b>Webseite</b>www.lindner-sportwetten.example</p>
  <div class="abs field" style="left:68px;top:2509px;width:165px;height:24px">Vollständiger Name</div>
  <div class="abs field" style="left:243px;top:2509px;width:165px;height:24px">E-Mail</div>
  <div class="abs field" style="left:68px;top:2540px;width:340px;height:101px">Deine Nachricht an uns</div>
  <div class="abs btn-send">Senden</div>
  <div class="abs bottom-bar"></div>
  <div class="abs copy">© 2020 Lindner Sportwetten.</div>
  <div class="abs bottom-nav">START<span>|</span>WETTTIPPS<span>|</span>ÜBER UNS<span>|</span>STATISTIK</div>
</footer>

</body>
</html>
```